Business Card for a Jewellery Brand

Business card for an upscale jewellery brand. Attached is the brand logo and icon and color board. I am looking for two card versions: one for the founder and one is generic. The card should be elegant and convey upscale and premium feel. I am open to both square and rectangle card shapes.

Industry/Entity Type

Jewelry

Contact Information for Business Card

Two cards: (1) Sunila Perumbadi (Founder) (2) General
(1) Sunila Perumbadi card should have Name: Sunila Perumbadi, Title: Founder Email id: sunila@quelm.com.au. Phone no: +61412555307
(2) Generic card should have Email id: info@quelm.com.au. Phone no: +61431555962

Requirements
Must have
• Workmark
• ICON
• Phone no
• Email ID
• ABN: 48917205563 (Note: ABN is Business number in Australia)
• Website: www.quelm.com.au
• Instagram: quelm_jewellery
• Facebook: @quelmjewellery
Nice to have
• Tagline

```html
<!DOCTYPE html>
<html lang="en">
<head>
<meta charset="utf-8">
<title>QUELM Business Cards</title>
<link href="https://fonts.googleapis.com/css2?family=Jost:wght@400;500;700&display=swap" rel="stylesheet">
<style>
  :root {
    --rose: #e0928a;
    --rose-deep: #d9756b;
    --rose-pale: #f6dcd8;
    --ink: #7a7a7a;
    --label: #b0b0b0;
    --value: #8a8a8a;
    --frame: #b5b5b5;
    --paper: #ffffff;
  }
  html, body {
    margin: 0;
    padding: 0;
    width: 1200px;
    height: 900px;
    overflow: hidden;
    background: var(--paper);
    font-family: "Jost", sans-serif;
  }
  .stage { position: relative; width: 1200px; height: 900px; }
  .card {
    position: absolute;
    top: 260px;
    width: 360px;
    height: 360px;
    box-sizing: border-box;
    border: 1px solid var(--frame);
    border-radius: 16px;
    background: var(--paper);
    overflow: hidden;
  }
  .card--founder { left: 40px; }
  .card--brand { left: 423px; }
  .card--general { left: 806px; }

  .facet-band { position: absolute; display: block; }

  .wordmark {
    position: absolute;
    left: 0; right: 0;
    text-align: center;
    color: var(--rose);
    font-weight: 400;
    letter-spacing: 0.28em;
    text-indent: 0.28em;
    margin: 0;
  }
  .card--founder .wordmark { top: 108px; font-size: 30px; }
  .card--brand .wordmark { top: 132px; font-size: 44px; }
  .card--general .wordmark { top: 128px; font-size: 30px; }

  .mark-square {
    position: absolute;
    left: 50%;
    background: var(--rose);
  }
  .card--founder .mark-square { top: 78px; width: 14px; height: 14px; margin-left: -7px; }
  .card--brand .mark-square { top: 88px; width: 20px; height: 20px; margin-left: -10px; }
  .card--general .mark-square { top: 94px; width: 14px; height: 14px; margin-left: -7px; }

  .founder-name {
    position: absolute;
    top: 156px; left: 0; right: 0;
    margin: 0;
    text-align: center;
    font-weight: 700;
    font-size: 18px;
    letter-spacing: 0.06em;
    color: var(--ink);
  }
  .name-rule {
    position: absolute;
    top: 183px; left: 48px; right: 48px;
    height: 2px;
    background: linear-gradient(90deg, transparent, var(--rose) 30%, var(--rose) 70%, transparent);
  }
  .contact {
    position: absolute;
    left: 0; right: 0;
    margin: 0;
    padding: 0;
    list-style: none;
    text-align: center;
    font-size: 16px;
    letter-spacing: 0.06em;
    line-height: 25px;
  }
  .contact .label { color: var(--label); }
  .contact .value { color: var(--value); }
  .card--founder .contact { top: 191px; font-size: 17px; }
  .card--general .contact { top: 194px; line-height: 21px; }
  .contact .gap { margin-top: 4px; }
  .contact .web {
    color: var(--rose-deep);
    font-weight: 700;
    letter-spacing: 0.1em;
    margin: 5px 0 4px;
  }
</style>
</head>
<body>
<main class="stage">

  <!-- Founder card -->
  <section class="card card--founder">
    <span class="mark-square"></span>
    <h1 class="wordmark">QUELM</h1>
    <h2 class="founder-name">Sunila Perumbadi</h2>
    <div class="name-rule"></div>
    <ul class="contact">
      <li><span class="label">email: </span><span class="value">sunila@quelm.com.au</span></li>
      <li><span class="label">phone: </span><span class="value">+61412555307</span></li>
    </ul>
    <svg class="facet-band" style="left:7px;top:228px" width="346" height="126" viewBox="0 0 346 126" role="img" aria-label="Faceted rose-pink gemstone pattern rising at both sides">
      <defs>
        <linearGradient id="facetFounder" x1="0" y1="0" x2="1" y2="0">
          <stop offset="0" stop-color="#e39a92"/>
          <stop offset="0.3" stop-color="#f3cbc6"/>
          <stop offset="0.5" stop-color="#fbeeed"/>
          <stop offset="0.7" stop-color="#f3cbc6"/>
          <stop offset="1" stop-color="#e39a92"/>
        </linearGradient>
      </defs>
      <path d="M0 0 H40 L70 60 H276 L306 0 H346 V126 H0 Z" fill="url(#facetFounder)"/>
    </svg>
  </section>

  <!-- Brand card -->
  <section class="card card--brand">
    <span class="mark-square"></span>
    <h1 class="wordmark">QUELM</h1>
    <svg class="facet-band" style="left:7px;top:160px" width="346" height="194" viewBox="0 0 346 194" role="img" aria-label="Faceted rose-pink gemstone pattern framing the base">
      <defs>
        <linearGradient id="facetBrand" x1="0" y1="0" x2="1" y2="0">
          <stop offset="0" stop-color="#e39a92"/>
          <stop offset="0.3" stop-color="#f0c1bb"/>
          <stop offset="0.5" stop-color="#fbeeed"/>
          <stop offset="0.7" stop-color="#f0c1bb"/>
          <stop offset="1" stop-color="#e39a92"/>
        </linearGradient>
      </defs>
      <path d="M0 0 H30 L60 70 H286 L316 0 H346 V194 H0 Z" fill="url(#facetBrand)"/>
    </svg>
  </section>

  <!-- General card -->
  <section class="card card--general">
    <svg class="facet-band" style="left:8px;top:8px" width="344" height="124" viewBox="0 0 344 124" role="img" aria-label="Faceted rose-pink gemstone pattern hanging from the top">
      <defs>
        <linearGradient id="facetGeneral" x1="0" y1="0" x2="1" y2="0">
          <stop offset="0" stop-color="#e39a92"/>
          <stop offset="0.3" stop-color="#f3cbc6"/>
          <stop offset="0.5" stop-color="#fbeeed"/>
          <stop offset="0.7" stop-color="#f3cbc6"/>
          <stop offset="1" stop-color="#e39a92"/>
        </linearGradient>
      </defs>
      <path d="M0 0 H344 V124 H310 L282 66 H62 L34 124 H0 Z" fill="url(#facetGeneral)"/>
    </svg>
    <span class="mark-square"></span>
    <h1 class="wordmark">QUELM</h1>
    <ul class="contact">
      <li><span class="label">Phone: </span><span class="value">+61431555962</span></li>
      <li><span class="label">Email: </span><span class="value">info@quelm.com.au</span></li>
      <li class="gap"><span class="label">ABN: </span><span class="value">48917205563</span></li>
      <li class="web">www.quelm.com.au</li>
      <li><span class="label">Instagram: </span><span class="value">quelm_jewellery</span></li>
      <li><span class="label">Facebook: </span><span class="value">@quelmjewellery</span></li>
    </ul>
  </section>

</main>
</body>
</html>
```